The Visual Personality of Miss Bayberry Food Trailer

Something that stands out with color and our logo. This is a food trailer that attends several events in the spring and summer. We are known for being one of the best Gumbo producers in mid Michigan. We have been responsible for connecting different communities and cultures together and we are strong supporters of our veterans since this is a veteran owned business. All of our vegetables are fresh and locally purchased. These recipes are originally from New Orleans Louisiana. Our website is Missbayberry.net. This will be used for an 8" x 11" poster. Leave a box or area that states "WHERE WE WILL BE:" so that we can add the location of the event that we are attending.

Target Market(s)

We do cuisine that is recognized in the southern states of the USA. but live in the northern part of the USA. We are providing a menu of different southern recipes so they do not have to go all the way down south for get..

Industry/Entity Type

Food/Restaurant Industry

Font styles to use
Serif
Decorative

Colors
0094D4
00A9DD
6FCCEA
C7EBF8
E9F6FB
59FF00
82FF00
B8FF75
E3FFCB
F4FFEA
FFF300
FFF600
FEFA6F
FFFEC7
FFFEE8
EE7325
F08F49
F5BC92
FAE3D3
FDF4ED
EB3D1F
EC4F4E
F09395
F8D3D4
FCEDEE
A7469A
B969AE
D3A5CF
EDDBEB
F8F0F9

Requirements
Must have
• Our logo, which is "Miss Bayberry", "Homemade Deliciousness". We need an area on the poster where we can manually add the location of the event we will be attending because it changes weekly. location
Nice to have
• Bold colors and logo

```html
<!DOCTYPE html>
<html lang="en">
<head>
<meta charset="utf-8">
<title>Miss Bayberry Food Trailer – Event Poster</title>
<link rel="stylesheet" href="https://fonts.googleapis.com/css2?family=Lobster&family=Open+Sans:wght@700&display=swap">
<style>
  :root {
    --page-bg: #e9e6e4;
    --poster-bg: #ffffff;
    --ink: #141414;
    --brand-red: #e3202a;
    --fresh-green: #7fc241;
    --label-white: #ffffff;
    --bread-light: #e3b77c;
    --bread-dark: #b8743a;
    --sandwich-red: #d9492e;
    --gumbo-orange: #e2723f;
    --gumbo-red: #c9462b;
    --gumbo-green: #8fae4a;
  }
  * { margin: 0; padding: 0; box-sizing: border-box; }
  html, body {
    width: 1200px;
    height: 1200px;
    overflow: hidden;
    background: var(--page-bg);
  }
  .poster {
    position: absolute;
    left: 193px;
    top: 40px;
    width: 620px;
    height: 853px;
    transform: scale(1.313);
    transform-origin: top left;
    background: var(--poster-bg);
    box-shadow: 0 4px 14px rgba(0,0,0,0.18);
    overflow: hidden;
  }
  .poster-art {
    position: absolute;
    inset: 0;
    width: 620px;
    height: 853px;
  }
  .brand {
    position: absolute;
    left: 360px;
    top: 70px;
    width: 240px;
    text-align: center;
  }
  .brand-dot {
    display: block;
    width: 54px;
    height: 54px;
    margin: 0 auto 10px;
    border-radius: 50%;
    background: var(--brand-red);
  }
  .brand-name {
    font-family: "Lobster", cursive;
    font-size: 34px;
    line-height: 1;
    color: var(--ink);
  }
  .headline {
    position: absolute;
    right: 55px;
    top: 280px;
    text-align: right;
    font-family: "Lobster", cursive;
    font-weight: 400;
    font-size: 39px;
    line-height: 47.5px;
    color: var(--ink);
  }
  .headline .accent-red { color: var(--brand-red); }
  .headline .accent-green { color: var(--fresh-green); font-size: 36px; }
  .location-label {
    position: absolute;
    left: 82px;
    top: 566px;
    font-family: "Open Sans", sans-serif;
    font-weight: 700;
    font-size: 13.5px;
    color: var(--label-white);
    letter-spacing: 0.2px;
  }
  .website {
    position: absolute;
    right: 55px;
    top: 770px;
    font-family: "Lobster", cursive;
    font-size: 29px;
    color: var(--ink);
  }
</style>
</head>
<body>
  <main class="poster">
    <svg class="poster-art" viewBox="0 0 620 853" xmlns="http://www.w3.org/2000/svg">
      <defs>
        <linearGradient id="sandwichTone" x1="0" y1="0" x2="1" y2="1">
          <stop offset="0" stop-color="#ead3a3"/>
          <stop offset="0.35" stop-color="#d79a5a"/>
          <stop offset="0.6" stop-color="#d9492e"/>
          <stop offset="1" stop-color="#b8743a"/>
        </linearGradient>
        <linearGradient id="gumboTone" x1="0" y1="0" x2="1" y2="1">
          <stop offset="0" stop-color="#8fae4a"/>
          <stop offset="0.4" stop-color="#e2723f"/>
          <stop offset="1" stop-color="#c9462b"/>
        </linearGradient>
      </defs>

      <path class="photo-sandwich" role="img" aria-label="Photo of a po' boy sandwich with fried fish, tomato, pickles and remoulade, with chips behind"
            fill="url(#sandwichTone)"
            d="M0 0 H350 C385 40 380 130 320 190 C270 240 232 272 258 318 C288 362 300 402 252 420 C200 436 100 402 0 352 Z"/>

      <path class="photo-gumbo" role="img" aria-label="Photo of a bowl of gumbo with okra, peppers and tomato"
            fill="url(#gumboTone)"
            d="M235 522 C300 500 352 540 422 530 C500 518 560 498 620 505 V690 C600 730 560 745 520 745 H300 C262 745 240 722 235 690 Z"/>

      <path class="swoosh" fill="#141414"
            d="M287 700 C330 690 390 700 425 718 C400 722 380 720 372 728 C350 730 320 722 292 716 C282 712 280 704 287 700 Z"/>

      <polygon class="location-card-shadow" fill="#141414" points="45,525 231,540 283,822 43,822"/>
      <polygon class="location-card" fill="var(--brand-red)" points="45,525 231,540 272,812 43,812"/>

      <g class="location-lines" stroke="#ffffff" stroke-width="1">
        <line x1="88" y1="628" x2="240" y2="628"/>
        <line x1="88" y1="657" x2="240" y2="657"/>
        <line x1="88" y1="685" x2="240" y2="685"/>
        <line x1="88" y1="713" x2="240" y2="713"/>
        <line x1="88" y1="741" x2="240" y2="741"/>
        <line x1="88" y1="770" x2="240" y2="770"/>
      </g>
    </svg>

    <div class="brand">
      <span class="brand-dot"></span>
      <div class="brand-name">Miss Bayberry</div>
    </div>

    <h1 class="headline">
      Homemade<br>
      <span class="accent-red">Deliciousness</span><br>
      created from<br>
      <span class="accent-green">fresh and authentic</span><br>
      ingredients.
    </h1>

    <p class="location-label">WHERE WE WILL BE</p>

    <p class="website">missbayberry.net</p>
  </main>
</body>
</html>
```